KVO-Business Card Design

I need a modern, professional business card design that includes my logo as the main feature, maybe the entire background with the contact info overlaying or even contact info on the back and the logo full frontal

Neat and organized placement of contact information

Would like to see options in black and white

Target Market(s)

real estate Developers, Construction managers, business and home owners

Industry/Entity Type

Construction

Contact Information for Business Card

KVO Construction
Danny Ferrante
General Contractor

Office: 1-888-902-7315 Ext #1
Cell: 215-730-4162
Fax: 1-888-902-7315

Font styles to use
Serif

Requirements
Must have
• title
• office #
• cell #
• Email
• website
Nice to have
• fax

```html
<!DOCTYPE html>
<html lang="en">
<head>
<meta charset="UTF-8">
<title>KVO Construction – Business Card</title>
<link rel="stylesheet" href="https://fonts.googleapis.com/css2?family=Roboto:wght@400;700&display=swap">
<style>
  :root {
    --page-bg: #d9d6d0;
    --card-black: #050505;
    --frame-green: #6cc04a;
    --brand-green: #5dbb3f;
    --green-light: #8fd35a;
    --green-mid: #2f9a3c;
    --green-dark: #0f5a24;
    --white: #ffffff;
  }
  * { box-sizing: border-box; margin: 0; padding: 0; }
  html, body {
    width: 1200px;
    height: 950px;
    overflow: hidden;
    background: var(--page-bg);
    font-family: "Roboto", Arial, sans-serif;
  }
  .canvas {
    position: relative;
    width: 1200px;
    height: 950px;
  }
  .card {
    position: absolute;
    width: 640px;
    height: 366px;
    box-shadow: 0 14px 30px rgba(0, 0, 0, 0.35);
  }
  .card-front {
    left: 150px;
    top: 70px;
    background: var(--card-black);
  }
  .card-back {
    left: 410px;
    top: 508px;
    background: radial-gradient(ellipse at 55% 45%, var(--green-light) 0%, var(--green-mid) 45%, var(--green-dark) 100%);
  }
  .card-frame {
    position: absolute;
    inset: 10px;
    border: 2px solid var(--frame-green);
  }
  .card-back .card-frame {
    border-color: var(--white);
  }
  .brand {
    position: absolute;
    inset: 0;
    display: flex;
    align-items: center;
    justify-content: center;
    gap: 16px;
  }
  .brand-mark {
    width: 34px;
    height: 34px;
    background: var(--brand-green);
  }
  .brand-name {
    font-size: 44px;
    font-weight: 700;
    color: var(--brand-green);
    letter-spacing: 1px;
  }
  .contact {
    position: absolute;
    left: 205px;
    top: 92px;
    color: var(--white);
  }
  .contact-mark {
    width: 26px;
    height: 26px;
    border: 3px solid var(--white);
    margin-bottom: 14px;
  }
  .contact-name {
    font-size: 25px;
    font-weight: 700;
    text-transform: uppercase;
    letter-spacing: 0.5px;
  }
  .contact-title {
    font-size: 17px;
    text-transform: uppercase;
    margin: 2px 0 18px;
  }
  .contact-line {
    font-size: 16px;
    line-height: 28px;
    white-space: nowrap;
  }
  .contact-line b {
    font-weight: 700;
    margin-right: 4px;
  }
  .contact-line .gap { margin-left: 12px; }
</style>
</head>
<body>
<main class="canvas">
  <section class="card card-front" aria-label="Card front">
    <div class="card-frame"></div>
    <div class="brand">
      <span class="brand-mark"></span>
      <span class="brand-name">KVO Construction</span>
    </div>
  </section>

  <section class="card card-back" aria-label="Card back">
    <div class="card-frame"></div>
    <div class="contact">
      <div class="contact-mark"></div>
      <div class="contact-name">Danny Ferrante</div>
      <div class="contact-title">General Contractor</div>
      <div class="contact-line"><b>O :</b>1-888-902-7315 Ext #1</div>
      <div class="contact-line"><b>C :</b>215-730-4162<span class="gap"><b>F :</b>1-888-902-7315</span></div>
      <div class="contact-line"><b>E :</b>danny@kvobuild.com<span class="gap"><b>W :</b>www.kvobuild.com</span></div>
    </div>
  </section>
</main>
</body>
</html>
```